Business Card Design Project

We are VT Meridian, a recruitment company based in London. We require a new business card design in order to present our business. We work in a number of areas recruiting professional in areas such as engineering and rail. Most of our work is based in the Middle East so our cards must have a universal, professional feel.

Visit our website: http://www.vt-meridian.example.co.uk/ for more info

Industry/Entity Type

Business

Requirements
Must have
• Must be double sided

Must feature the companies logo on both sides of the card

Should incorporate the primary colours of the logo

Must be professional and contemporary, to fit in with the logo

Info: Name: Colin Prewett certRP MREC
Senior Recruitment Consultant
Address: 7 Quarry Row Fulwell London N41QZ
T: +44 (0)203 555 0147
M: +44 (0)7700 900 318
E: cprewett@vt-meridian.example.co.uk
W www.vt-meridian.example.co.uk
Nice to have
• A modern style card

```html
<!DOCTYPE html>
<html lang="en">
<head>
<meta charset="utf-8">
<title>VT Meridian – Business Card</title>
<link href="https://fonts.googleapis.com/css2?family=EB+Garamond:wght@400&family=Quicksand:wght@500&display=swap" rel="stylesheet">
<style>
  :root {
    --brand-green: #3fdc82;
    --brand-green-pale: #c9f4dc;
    --brand-grey: #7f878c;
    --ink: #1e1e1e;
    --card: #ffffff;
    --backdrop: #2b2d2e;
  }
  html, body {
    margin: 0;
    padding: 0;
    width: 1200px;
    height: 900px;
    overflow: hidden;
    background: var(--backdrop);
  }
  .canvas {
    position: relative;
    width: 1200px;
    height: 900px;
  }
  .card {
    position: absolute;
    top: 285px;
    width: 520px;
    height: 330px;
    background: var(--card);
    overflow: hidden;
  }
  .card--front { left: 60px; }
  .card--back { left: 620px; }

  .brand {
    position: absolute;
    display: flex;
    align-items: center;
    font-family: "Quicksand", sans-serif;
    font-weight: 500;
    color: var(--brand-grey);
    white-space: nowrap;
  }
  .brand__dot {
    border-radius: 50%;
    background: var(--brand-green);
    flex: none;
  }
  .card--front .brand { left: 42px; top: 34px; font-size: 30px; letter-spacing: -0.5px; }
  .card--front .brand__dot { width: 34px; height: 34px; margin-right: 8px; }
  .card--back .brand { left: 44px; top: 58px; font-size: 50px; letter-spacing: -1px; }
  .card--back .brand__dot { width: 56px; height: 56px; margin-right: 12px; }

  .accent-bar {
    position: absolute;
    background: var(--brand-green);
  }
  .card--front .accent-bar--left { left: 0; top: 100px; width: 14px; height: 160px; }
  .card--front .accent-bar--right { right: 0; top: 12px; width: 14px; height: 160px; }
  .card--front .divider { left: 352px; top: 22px; width: 5px; height: 286px; border-radius: 3px; }
  .card--back .accent-bar--left { left: 0; top: 70px; width: 22px; height: 180px; }

  .watermark-shape {
    position: absolute;
    border-radius: 50%;
    background: var(--brand-green-pale);
  }
  .card--front .watermark-shape { left: 408px; top: 190px; width: 120px; height: 120px; }
  .card--back .watermark-shape { left: 330px; top: 160px; width: 150px; height: 150px; }

  .person {
    position: absolute;
    left: 62px;
    top: 94px;
    font-family: "EB Garamond", serif;
    color: var(--ink);
  }
  .person__name { margin: 0; font-size: 17px; font-weight: 400; }
  .person__role { margin: 8px 0 0; font-size: 13.5px; }

  .contact {
    position: absolute;
    left: 62px;
    top: 226px;
    margin: 0;
    font-family: "EB Garamond", serif;
    font-size: 11.5px;
    line-height: 1.35;
    color: var(--ink);
  }
  .contact__gap { margin-top: 9px; }
  .contact p { margin: 0; }
</style>
</head>
<body>
<main class="canvas">

  <section class="card card--front" aria-label="Business card, front">
    <div class="brand"><span class="brand__dot"></span>VT Meridian</div>
    <div class="accent-bar accent-bar--left"></div>
    <div class="accent-bar divider"></div>
    <div class="accent-bar accent-bar--right"></div>
    <div class="watermark-shape"></div>

    <div class="person">
      <h1 class="person__name">Colin Prewett certRP MREC</h1>
      <p class="person__role">Senior Recruitment Consultant</p>
    </div>

    <address class="contact">
      <p>T: +44 (0)203 555 0147</p>
      <p>M: +44 (0)7700 900 318</p>
      <p>Address: 7 Quarry Row Fulwell London N41QZ</p>
      <p class="contact__gap">E: cprewett@vt-meridian.example.co.uk</p>
      <p>W www.vt-meridian.example.co.uk</p>
    </address>
  </section>

  <section class="card card--back" aria-label="Business card, back">
    <div class="accent-bar accent-bar--left"></div>
    <div class="brand"><span class="brand__dot"></span>VT Meridian</div>
    <div class="watermark-shape"></div>
  </section>

</main>
</body>
</html>
```